Amber Heron Fund Pitch Deck

This is a PowerPoint for use in investor presentations. The copy is written (although it may have small tweaks) and the designer will be responsible for creating a template and some graphical representations inside the presentation.

Note on the logo. Only the Amber Heron should be used, not the text.

```html
<!DOCTYPE html>
<html lang="en">
<head>
<meta charset="utf-8">
<title>Amber Heron NPL Fund — Pitch Deck</title>
<link href="https://fonts.googleapis.com/css2?family=Poppins:wght@300;400;500;600;700;800&display=swap" rel="stylesheet">
<style>
:root{
  --page:#f2f2f2;
  --white:#ffffff;
  --ink:#1f2330;
  --muted:#5d6270;
  --faint:#9aa0ad;
  --blue:#5b7fc7;
  --blue-deep:#2e4f9e;
  --navy:#0c1c40;
  --orange:#f6a21e;
  --line:#b9c6e6;
  --band:#e9e9ec;
  --pill:#3b3d44;
}
*{box-sizing:border-box;margin:0;padding:0}
html,body{width:1200px;height:2489px;overflow:hidden;background:var(--page);font-family:'Poppins',sans-serif;color:var(--ink)}
.deck{position:absolute;left:32px;top:32px;display:grid;grid-template-columns:554px 554px;grid-auto-rows:311px;column-gap:30px;row-gap:29.5px}
.slide{position:relative;width:554px;height:311px;background:var(--white);overflow:hidden}
.abs{position:absolute}
.photo{position:absolute}
.heading{position:absolute;left:32px;font-size:14px;font-weight:700;color:var(--ink)}
.heading span{color:var(--blue)}
.heading::before{content:"";position:absolute;left:0;top:-8px;width:28px;height:2px;background:var(--blue)}
.heading.centered::before{display:none}
.heading.light{color:var(--white)}
.heading.light span{color:#8fb0ee}
.footer-brand{position:absolute;left:32px;top:277px;font-size:7px;font-weight:600;color:var(--blue)}
.footer-line{position:absolute;left:32px;right:32px;top:289px;height:1px;background:var(--line)}
.copyright{position:absolute;right:32px;top:280px;font-size:5.5px;color:var(--faint)}
.dark .copyright{color:#8a97b8}
.dark .footer-brand{color:#7f9fe0}
.dark .footer-line{background:#3c5590}
.title-lockup{position:absolute;font-weight:700;line-height:1.05;text-align:left}
.small{font-size:6px;line-height:1.45;color:var(--muted)}
.small b{color:var(--ink)}
.bullets{list-style:none}
.bullets li{position:relative;padding-left:11px;margin-bottom:5px;font-size:6.2px;line-height:1.4;color:var(--muted)}
.bullets li b{color:var(--ink)}
.bullets.chev li::before{content:"»";position:absolute;left:0;top:-1px;color:var(--blue);font-size:8px}
.bullets.dot li::before{content:"";position:absolute;left:1px;top:1.5px;width:5px;height:5px;border-radius:50%;border:1.2px solid var(--blue)}
.bullets.whitedot li{color:#dfe5f3}
.bullets.whitedot li::before{content:"";position:absolute;left:1px;top:2px;width:4.5px;height:4.5px;border-radius:50%;background:var(--white)}
.card{position:absolute;background:var(--white);border-radius:6px;box-shadow:0 2px 10px rgba(30,50,100,.12);padding:36px 10px 8px}
.avatar{position:absolute;width:40px;height:40px;border-radius:50%;border:2px solid var(--blue);background:linear-gradient(160deg,#d9dde5,#9aa3b4)}
.card .name{text-align:center;font-size:6.5px;font-weight:600;color:var(--blue)}
.card .role{text-align:center;font-size:5.5px;color:var(--muted);margin-bottom:12px;padding-bottom:5px;border-bottom:1px solid #e3e6ee}
.card .bullets li{font-size:5.2px;margin-bottom:4px}
.stat-label{font-size:6px;color:#d7def0}
.stat{font-size:14px;font-weight:700;color:var(--orange)}
.stat small{font-size:6px;color:var(--white);font-weight:600}
.step-text{position:absolute;width:90px;text-align:center;font-size:5.6px;line-height:1.35;color:var(--ink)}
.adv-tag{position:absolute;height:42px;width:150px;background:linear-gradient(90deg,var(--blue-deep),#1e4fb3);transform:skewX(-18deg);box-shadow:4px 4px 0 rgba(255,255,255,.7)}
.adv-tag span{display:block;transform:skewX(18deg);text-align:center;line-height:42px;color:var(--white);font-weight:700;font-size:18px}
.mgmt-row{position:absolute;left:360px;width:170px;height:36px;border-bottom:1px solid #d5dbe8}
.mgmt-row .avatar{width:30px;height:30px;left:0;top:2px;border-width:1.5px}
.mgmt-row .n{position:absolute;left:42px;top:9px;font-size:6.2px;font-weight:600;color:var(--blue)}
.mgmt-row .r{position:absolute;left:42px;top:18px;font-size:5.2px;color:var(--muted)}
.big-amount{position:absolute;font-weight:700;color:var(--blue-deep);font-size:40px;line-height:1}
.big-amount sup{font-size:16px;color:var(--orange);vertical-align:top;position:relative;top:4px}
.amount-unit{position:absolute;font-size:7px;font-weight:700;color:var(--ink)}
.amount-note{position:absolute;font-size:5.5px;color:var(--muted);text-align:center;width:100px;line-height:1.35}
</style>
</head>
<body>
<main class="deck">

  <section class="slide cover-light">
    <div class="photo" role="img" aria-label="Business handshake over a city skyline with light digital overlay" style="inset:0;background:linear-gradient(180deg,#f4f6fa 0%,#dde3ec 45%,#b9c2d0 70%,#d8c2ad 85%,#e7ebf1 100%)"></div>
    <div class="title-lockup" style="left:190px;top:128px;color:var(--blue-deep);font-size:26px">Amber Heron<br>NPL Fund</div>
  </section>

  <section class="slide cover-dark">
    <div class="photo" role="img" aria-label="Night city skyline with glowing data lines" style="inset:0;background:radial-gradient(ellipse at 60% 45%,#2a5d86 0%,#10324f 45%,#06182b 100%)"></div>
    <div class="title-lockup" style="left:200px;top:142px;color:var(--white);font-size:28px">Amber Heron<br>NPL Fund</div>
  </section>

  <section class="slide cover-blue">
    <div class="photo" role="img" aria-label="Businessman with a tablet behind a blue network graphic" style="inset:0;background:linear-gradient(135deg,#2b4f9e 0%,#4d7ed1 40%,#9ec0ea 70%,#3c66b8 100%)"></div>
    <div class="title-lockup" style="left:198px;top:140px;color:var(--white);font-size:28px">Amber Heron<br>NPL Fund</div>
  </section>

  <section class="slide edge">
    <h2 class="heading" style="top:62px">The <span>Edge</span></h2>
    <ul class="bullets chev abs" style="left:32px;top:112px;width:210px">
      <li>Experience with <b>fund management</b> and <b>asset disposal.</b></li>
      <li>Utilizing the clues and hints that borrowers and guarantors leave on the internet, we can <b>special service assets</b> and collect on them <b>more quickly</b> and <b>maximize return.</b></li>
      <li>Much of the <b>technology</b> and <b>experience</b> as a team can be attributed to the team's experience at Brightfield.</li>
      <li>The principals were the management team that came on in March 2020 and grew the business <b>from less than</b></li>
    </ul>
    <div class="abs" style="left:43px;top:208px;font-size:12px;font-weight:600;color:var(--orange)">12,000 PPP <span style="font-size:6px;color:var(--ink);font-weight:700">loans to more than</span> <span style="color:var(--blue)">800,000</span></div>
    <div class="photo" role="img" aria-label="Silhouettes of business people at a window facing city towers" style="left:290px;top:92px;width:236px;height:146px;background:linear-gradient(180deg,#6f8aa8 0%,#3b4e66 55%,#0d1118 100%)"></div>
    <div class="footer-brand">Amber Heron</div>
    <div class="copyright">© 2022 Copyright Amber Heron NPL Fund - All Rights Reserved</div>
    <div class="footer-line"></div>
  </section>

  <section class="slide technology">
    <h2 class="heading" style="top:62px">The <span>Technology</span></h2>
    <p class="small abs" style="left:32px;top:104px;width:190px">Most lenders and servicers use Norvask or Servora and then software like Tessaro for collections.</p>
    <p class="small abs" style="left:32px;top:126px;width:195px">These software packages fail to address the most important factors which is to analyze the borrower (and the guarantors) to allow for customized collection plans. <b>We use enhanced skip tracing developed during PPP forgiveness and collection efforts with advanced social media logic.</b></p>
    <div class="abs" style="left:0;top:191px;width:240px;height:50px;background:var(--blue);padding:17px 0 0 32px;font-size:6px;font-weight:600;color:var(--white);line-height:1.4">Finally, we use evolving algorithms to price and<br>purchase NPL portfolios at the correct price.</div>
    <div class="photo" role="img" aria-label="Analyst at a desk with printed bar charts, calculator and keyboard" style="left:264px;top:51px;width:290px;height:190px;background:linear-gradient(135deg,#8a7f74 0%,#cfc6bb 40%,#8aa7d6 60%,#4a5565 100%)"></div>
    <div class="footer-brand">Amber Heron</div>
    <div class="copyright">© 2022 Copyright Amber Heron NPL Fund - All Rights Reserved</div>
    <div class="footer-line"></div>
  </section>

  <section class="slide people-two">
    <h2 class="heading" style="top:40px">The <span>People</span></h2>
    <article class="card" style="left:52px;top:88px;width:200px;height:175px">
      <div class="name">Grant Whitlow</div>
      <div class="role">Managing Partner, Investment Committee</div>
      <ul class="bullets dot">
        <li>More than 20 years of banking experience with Harbor Lynd, Union National Bank and Tri-State Bank</li>
        <li>Director of Halvorsen Capital Management, in less than 5 years, achieved 4x AUM and outsized returns managing distressed asset fund. Developed framework for additional funds.</li>
        <li>CEO of Brightfield.</li>
      </ul>
    </article>
    <div class="avatar" role="img" aria-label="Portrait photo of Grant Whitlow" style="left:132px;top:68px"></div>
    <article class="card" style="left:302px;top:88px;width:200px;height:175px">
      <div class="name">Nathan Corwell</div>
      <div class="role">Managing Partner, Investment Committee</div>
      <ul class="bullets dot">
        <li>Founder of Meridian Law in Scottsdale, which became the first law firm in the country sold to private non-lawyer investors.</li>
        <li>Extensive experience with large transactions, including a major bankruptcy sale for a client. Speaker at industry bankruptcy conferences.</li>
        <li>COO of Vantiq, an early web development company that built a successful e-commerce campaign and association software.</li>
        <li>General Counsel of Brightfield.</li>
      </ul>
    </article>
    <div class="avatar" role="img" aria-label="Portrait photo of Nathan Corwell" style="left:382px;top:68px"></div>
    <div class="footer-brand">Amber Heron</div>
    <div class="copyright">© 2022 Copyright Amber Heron NPL Fund - All Rights Reserved</div>
    <div class="footer-line"></div>
  </section>

  <section class="slide people-three">
    <h2 class="heading" style="top:40px">The <span>People</span></h2>
    <article class="card" style="left:30px;top:88px;width:156px;height:175px">
      <div class="name">Owen Delacroix</div>
      <div class="role">Investment Committee</div>
      <ul class="bullets dot">
        <li>CEO of Northgate Impact Corp (Symbol: NGIC)</li>
        <li>CEO, ArcBank</li>
        <li>Director, KeyMark Bank</li>
        <li>Member, Pellham Directors Circle</li>
      </ul>
    </article>
    <div class="avatar" role="img" aria-label="Portrait photo of Owen Delacroix" style="left:88px;top:68px"></div>
    <article class="card" style="left:200px;top:88px;width:156px;height:175px">
      <div class="name">Peter Lindqvist</div>
      <div class="role">Director of Credit Analytics</div>
      <ul class="bullets dot">
        <li>Product and data specialist with more than 15 years technology and startup experience.</li>
        <li>Founded a communications firm which combined email and chat for customer success teams. Raised capital and served 40,000 users.</li>
        <li>Led advertising products at a media firm and grew revenue from $7 million to $45 million over 5 years.</li>
        <li>Advisory Board member with venture capital firm.</li>
        <li>VP, Products, Brightfield.</li>
      </ul>
    </article>
    <div class="avatar" role="img" aria-label="Portrait photo of Peter Lindqvist" style="left:258px;top:68px"></div>
    <article class="card" style="left:370px;top:88px;width:156px;height:175px">
      <div class="name">Ryan Tolliver</div>
      <div class="role">Chief Operating Officer</div>
      <ul class="bullets dot">
        <li>Management Consultant at Alder &amp; Company and Marston LLP</li>
        <li>Founder of two companies that grew to more than 1,000 employees.</li>
        <li>COO of Brightfield.</li>
      </ul>
    </article>
    <div class="avatar" role="img" aria-label="Portrait photo of Ryan Tolliver" style="left:428px;top:68px"></div>
    <div class="footer-brand">Amber Heron</div>
    <div class="copyright">© 2022 Copyright Amber Heron NPL Fund - All Rights Reserved</div>
    <div class="footer-line"></div>
  </section>

  <section class="slide market dark">
    <div class="photo" role="img" aria-label="Business people silhouetted in a dark blue office with network lines" style="inset:0;background:linear-gradient(135deg,#0e2350 0%,#0a1a3d 50%,#163a78 100%)"></div>
    <h2 class="heading light" style="top:40px">The <span>Market</span></h2>
    <div class="abs" style="left:34px;top:72px">
      <div class="stat-label">The commercial lending market size was valued at</div>
      <div class="stat">$8,823.53 <small>billion</small> <small style="font-weight:400">in 2020</small></div>
    </div>
    <div class="abs" style="left:34px;top:142px">
      <div class="stat-label">is projected to reach</div>
      <div class="stat">$29,379.83 <small>billion</small> <small style="font-weight:400">by 2030</small></div>
    </div>
    <div class="abs" style="left:34px;top:199px">
      <div class="stat-label">growing at a CAGR of</div>
      <div class="stat">13.1% <small style="font-weight:400">from 2021 to 2030</small></div>
    </div>
    <div class="abs" style="left:34px;top:250px;font-size:5px;color:#c7d0e6;font-style:italic">Source: https://www.example-research.com/commercial-lending-market</div>
    <div class="abs" style="left:310px;top:108px;font-size:44px;font-weight:700;color:#4a6aa8;line-height:1">“</div>
    <div class="abs" style="left:335px;top:130px;width:160px;font-size:7.3px;font-weight:700;color:var(--white);text-align:center;line-height:1.4">The credit cycle is entering into a period of rising interest rates and corresponding defaults. The fund seeks to take advantage of that emerging opportunity.</div>
    <div class="footer-brand">Amber Heron</div>
    <div class="copyright">© 2022 Copyright Amber Heron NPL Fund - All Rights Reserved</div>
    <div class="footer-line"></div>
  </section>

  <section class="slide process">
    <h2 class="heading centered" style="top:40px;left:0;width:554px;text-align:center">Our <span>Process</span></h2>
    <div class="abs" style="left:263px;top:32px;width:28px;height:2px;background:var(--blue)"></div>
    <div class="abs" style="left:0;top:146px;width:554px;height:19px;background:var(--band)"></div>
    <div class="step-text" style="left:45px;top:78px">Work with our lender customers on their non-performing loan portfolio.</div>
    <div class="step-text" style="left:168px;top:78px">Provide special servicing in compliance with bank's servicing criteria.</div>
    <div class="step-text" style="left:291px;top:78px">Maintain first right of refusal to purchase loan using proprietary algorithm.</div>
    <div class="step-text" style="left:414px;top:94px">Liquidation, when necessary.</div>
    <div class="step-text" style="left:109px;top:210px">Purchase participation in non-performing loans.</div>
    <div class="step-text" style="left:232px;top:210px">Provide bank access to NPL platform.</div>
    <div class="step-text" style="left:355px;top:210px">Internal servicing standards.</div>
    <svg class="abs" style="left:0;top:0" width="554" height="311" viewBox="0 0 554 311">
      <defs>
        <g id="pin"><path d="M0 -13 C7 -13 11 -8 11 -2 C11 6 0 13 0 13 C0 13 -11 6 -11 -2 C-11 -8 -7 -13 0 -13Z" fill="#5b7fc7"/><rect x="-1.5" y="-18" width="3" height="6" rx="1" fill="#5b7fc7"/></g>
      </defs>
      <g font-family="Poppins,sans-serif" font-size="10" font-weight="700" fill="#fff" text-anchor="middle">
        <use href="#pin" x="90" y="137"/><text x="90" y="140">1</text>
        <use href="#pin" x="213" y="137"/><text x="213" y="140">3</text>
        <use href="#pin" x="336" y="137"/><text x="336" y="140">5</text>
        <use href="#pin" x="459" y="137"/><text x="459" y="140">8</text>
        <use href="#pin" x="154" y="187"/><text x="154" y="190">2</text>
        <use href="#pin" x="277" y="187"/><text x="277" y="190">4</text>
        <use href="#pin" x="400" y="187"/><text x="400" y="190">6</text>
      </g>
    </svg>
    <div class="abs" style="left:90px;top:244px;width:374px;height:28px;border-radius:14px;background:var(--pill);color:var(--white);font-size:5.6px;text-align:center;padding-top:7px;line-height:1.35">Initially partner with licensed collection agencies to supplement our in-house abilities (and<br>comply with regulatory requirements). Potential to acquire and bring completely in-house.</div>
    <div class="footer-brand" style="top:279px">Amber Heron</div>
    <div class="copyright">© 2022 Copyright Amber Heron NPL Fund - All Rights Reserved</div>
    <div class="footer-line"></div>
  </section>

  <section class="slide customers dark">
    <div class="photo" role="img" aria-label="Dark navy background with scattered faint people icons" style="inset:0;background:linear-gradient(135deg,#182c5c 0%,#0e1f48 55%,#0a1736 100%)"></div>
    <h2 class="heading light" style="top:40px">Our <span>Customers</span></h2>
    <div class="abs" style="left:32px;top:88px;font-size:6px;font-weight:700;color:var(--white)">Target Market</div>
    <div class="abs" style="left:32px;top:111px"><div class="stat-label">Community banks</div><div class="stat" style="font-size:15px">Nearly 5,000</div></div>
    <div class="abs" style="left:190px;top:111px"><div class="stat-label">Mid-Market banks</div><div class="stat" style="font-size:15px">Approximately 4,000</div></div>
    <div class="footer-brand">Amber Heron</div>
    <div class="copyright">© 2022 Copyright Amber Heron NPL Fund - All Rights Reserved</div>
    <div class="footer-line"></div>
  </section>

  <section class="slide advantage dark">
    <div class="photo" role="img" aria-label="Businessman's hand pointing at a glowing city and network graphic" style="inset:0;background:linear-gradient(135deg,#e8edf4 0%,#c7d2e3 40%,#8aa3c7 65%,#3f5f98 100%)"></div>
    <h2 class="heading" style="top:40px">Advantage</h2>
    <svg class="abs" style="left:80px;top:102px" width="46" height="46" viewBox="0 0 46 46" fill="none" stroke="#2e55b3" stroke-width="2">
      <circle cx="23" cy="23" r="7"/><circle cx="23" cy="6" r="3.5"/><circle cx="23" cy="40" r="3.5"/><circle cx="7" cy="14" r="3.5"/><circle cx="39" cy="14" r="3.5"/><circle cx="7" cy="32" r="3.5"/><circle cx="39" cy="32" r="3.5"/>
      <path d="M23 9.5V16M23 30v6.5M10 16l7 4M36 16l-7 4M10 30l7-4M36 30l-7-4"/>
    </svg>
    <svg class="abs" style="left:268px;top:100px" width="48" height="48" viewBox="0 0 48 48" fill="none" stroke="#2e55b3" stroke-width="2">
      <path d="M16 10h12l-3 6H19z"/><path d="M19 16C10 22 8 40 22 40h6c10 0 10-18 0-24"/>
      <text x="22" y="33" font-family="Poppins,sans-serif" font-size="13" font-weight="700" fill="#2e55b3" stroke="none" text-anchor="middle">$</text>
      <rect x="30" y="30" width="14" height="4" rx="1"/><rect x="30" y="35" width="14" height="4" rx="1"/><rect x="30" y="40" width="14" height="4" rx="1"/>
    </svg>
    <div class="adv-tag" style="left:36px;top:163px"><span>Tech</span></div>
    <div class="adv-tag" style="left:220px;top:163px"><span>Capital</span></div>
    <div class="footer-brand">Amber Heron</div>
    <div class="copyright">© 2022 Copyright Amber Heron NPL Fund - All Rights Reserved</div>
    <div class="footer-line"></div>
  </section>

  <section class="slide management">
    <div class="photo" role="img" aria-label="Dark navy panel with abstract network lines" style="left:0;top:0;width:327px;height:311px;background:linear-gradient(160deg,#163066 0%,#0c1d44 60%,#0a1836 100%)"></div>
    <div class="avatar" role="img" aria-label="Portrait photo of Grant Whitlow" style="left:127px;top:54px;width:74px;height:74px;border:3px solid var(--white)"></div>
    <div class="abs" style="left:0;width:327px;top:150px;text-align:center;font-size:7.5px;font-weight:600;color:var(--white)">Grant Whitlow</div>
    <div class="abs" style="left:0;width:327px;top:161px;text-align:center;font-size:5.5px;color:#c9d3ea">Managing Partner, Investment Committee</div>
    <ul class="bullets whitedot abs" style="left:74px;top:186px;width:180px">
      <li>More than 20 years of banking experience with Harbor Lynd, Union National Bank and Tri-State Bank</li>
      <li>Director of Halvorsen Capital Management, in less than 5 years, achieved 4x AUM and outsized returns managing distressed asset fund. Developed framework for additional funds.</li>
      <li>CEO of Brightfield.</li>
    </ul>
    <h2 class="heading" style="top:40px;left:356px">Management <span>Structure</span></h2>
    <div class="mgmt-row" style="top:66px"><div class="avatar" role="img" aria-label="Portrait photo of Grant Whitlow"></div><div class="n">Grant Whitlow</div><div class="r">Managing Partner, Investment Committee</div></div>
    <div class="mgmt-row" style="top:104px"><div class="avatar" role="img" aria-label="Portrait photo of Nathan Corwell"></div><div class="n">Nathan Corwell</div><div class="r">Managing Partner, Investment Committee</div></div>
    <div class="mgmt-row" style="top:144px"><div class="avatar" role="img" aria-label="Portrait photo of Owen Delacroix"></div><div class="n">Owen Delacroix</div><div class="r">Investment Committee</div></div>
    <div class="mgmt-row" style="top:184px"><div class="avatar" role="img" aria-label="Portrait photo of Peter Lindqvist"></div><div class="n">Peter Lindqvist</div><div class="r">Director of Credit Analytics</div></div>
    <div class="mgmt-row" style="top:224px"><div class="avatar" role="img" aria-label="Portrait photo of Ryan Tolliver"></div><div class="n">Ryan Tolliver</div><div class="r">Chief Operating Officer</div></div>
    <div class="abs" style="left:470px;top:276px;font-size:7px;font-weight:600;color:var(--blue)">Amber Heron</div>
  </section>

  <section class="slide cosponsor">
    <div class="photo" role="img" aria-label="Faded business people in a bright office" style="left:0;top:0;width:340px;height:311px;background:linear-gradient(90deg,#f6f7f9 0%,#e3e6eb 45%,#f7f8fa 100%)"></div>
    <h2 class="heading" style="top:132px;line-height:1.2">Northgate<br><span>Co-Sponsored Fund</span></h2>
    <p class="small abs" style="left:32px;top:168px;width:180px">Utilize Northgate network, AMHR technology. Joint LP investment, Northgate affiliates / partners to provide additional LP investment</p>
    <svg class="abs" style="left:305px;top:70px" width="140" height="140" viewBox="0 0 140 140">
      <circle cx="70" cy="70" r="58" fill="none" stroke="#2e4f9e" stroke-width="14" stroke-dasharray="291.6 364.4" transform="rotate(-18 70 70)"/>
      <circle cx="70" cy="70" r="58" fill="none" stroke="#f6a21e" stroke-width="14" stroke-dasharray="72.9 364.4" stroke-dashoffset="-291.6" transform="rotate(-18 70 70)"/>
      <text x="70" y="67" text-anchor="middle" font-family="Poppins,sans-serif" font-size="8.5" font-weight="600" fill="#5b7fc7">NPL Heron,</text>
      <text x="70" y="79" text-anchor="middle" font-family="Poppins,sans-serif" font-size="8.5" font-weight="600" fill="#5b7fc7">LLC to be GP</text>
    </svg>
    <div class="abs" style="left:442px;top:74px;font-size:20px;font-weight:700;color:var(--orange)">20%</div>
    <div class="abs" style="left:442px;top:100px;font-size:5.5px;color:var(--muted)">to Northgate</div>
    <div class="abs" style="left:245px;top:176px;font-size:20px;font-weight:700;color:var(--blue)">80%</div>
    <div class="abs" style="left:245px;top:202px;font-size:5.5px;color:var(--muted)">of carry to AMHR</div>
    <div class="footer-brand">Amber Heron</div>
    <div class="copyright">© 2022 Copyright Amber Heron NPL Fund - All Rights Reserved</div>
    <div class="footer-line"></div>
  </section>

  <section class="slide fund-size">
    <div class="photo" role="img" aria-label="Young plant growing from a glass jar of coins" style="left:318px;top:0;width:236px;height:311px;background:linear-gradient(160deg,#dfeec0 0%,#a7cf6e 40%,#6d9a3e 70%,#c9d4b5 100%)"></div>
    <div class="abs" style="left:32px;top:55px;width:28px;height:2px;background:var(--blue)"></div>
    <div class="abs" style="left:32px;top:62px;font-size:13px;color:var(--ink)">Projected Size of Fund</div>
    <div class="abs" style="left:32px;top:78px;font-size:13px;font-weight:600;color:var(--blue)">Initially $200 million, up to $1 billion</div>
    <div class="big-amount" style="left:36px;top:160px"><sup>$</sup>100</div>
    <div class="amount-unit" style="left:94px;top:196px">Million</div>
    <div class="amount-note" style="left:42px;top:208px">commitment from AMHR<br>from funds due from CPF</div>
    <div class="big-amount" style="left:178px;top:160px"><sup>$</sup>100</div>
    <div class="amount-unit" style="left:236px;top:196px">Million</div>
    <div class="amount-note" style="left:184px;top:208px">commitment from<br>Northgate or its affiliates</div>
    <div class="footer-brand">Amber Heron</div>
    <div class="copyright">© 2022 Copyright Amber Heron NPL Fund - All Rights Reserved</div>
    <div class="footer-line"></div>
  </section>

</main>
</body>
</html>
```